Thimble Deli Needs a Web Page!

Thimble Deli is a gourmet sandwich shop in Baltimore, MD USA.
We are due to open in about a month or so and we need a great web page that looks cool and is easy to use. Our Concept supports local farmers, ranchers, fishmongers & purveyors. All of our menu items are made from scratch using fresh local ingredients.

Target Market(s)

Urban people on the go & Anyone who is hungry and likes a great sandwich

Industry/Entity Type

Shop

Requirements
Must have
• We must have these 8 tabs:
Home
Menus
Gallery
About Us
Media & Events
Hours & Location
Order Online
Contact Us

Also we would like our Logo to be a focal point
Our Color scheme is Red, Black, Grey, White and a reddish-orange
however any and all colors are great and will be considered
We would love an area on the page for our own food photos to be added.
Nice to have
• Baltimore Skyline
Order Online Now Button
Free Wi-Fi Symbol
Dine-In, Take Out, Delivery,
Business Lunches, Tail Gate Platters, Catering
Should not have
• No Stock images of food or chefs.
(We want to put all of our own food photos up later.)
No Pink.

```html
<!DOCTYPE html>
<html lang="en">
<head>
<meta charset="utf-8">
<title>Thimble Deli — About Us</title>
<link rel="stylesheet" href="https://fonts.googleapis.com/css2?family=Lobster+Two:ital,wght@1,700&family=PT+Sans:wght@400;700&display=swap">
<style>
  :root {
    --wood-dark: #2a160d;
    --wood-mid: #5a3520;
    --plate-light: #d8cfc4;
    --candle: #f3d9a0;
    --band: rgba(235, 235, 235, 0.82);
    --panel: rgba(255, 255, 255, 0.74);
    --panel-edge: rgba(255, 255, 255, 0.9);
    --ink: #3d3d3d;
    --ink-soft: #4a4a4a;
    --accent: #7c2a36;
    --brand-red: #c8202a;
    --close-grey: #b4b4b4;
    --white: #ffffff;
  }
  * { box-sizing: border-box; margin: 0; padding: 0; }
  html, body { width: 1200px; height: 800px; overflow: hidden; }
  body {
    position: relative;
    font-family: "PT Sans", Tahoma, sans-serif;
    color: var(--ink);
    background: var(--wood-dark);
  }
  .backdrop {
    position: absolute; inset: 0;
    background:
      radial-gradient(ellipse 380px 260px at 1080px 300px, var(--candle), transparent 70%),
      radial-gradient(ellipse 620px 360px at 560px 520px, var(--plate-light), transparent 72%),
      radial-gradient(ellipse 500px 300px at 200px 120px, #9c8a7c, transparent 70%),
      linear-gradient(160deg, var(--wood-mid), var(--wood-dark));
  }
  .brand {
    position: absolute; top: 58px; left: 0; width: 1200px;
    display: flex; justify-content: center; align-items: center; gap: 14px;
  }
  .brand-dot { width: 64px; height: 64px; border-radius: 50%; background: var(--brand-red); }
  .brand-name {
    font-family: "PT Sans", Tahoma, sans-serif; font-weight: 700;
    font-size: 44px; color: var(--white); letter-spacing: 1px;
  }
  .wifi-badge {
    position: absolute; left: 930px; top: 106px; width: 62px; height: 44px;
    border-radius: 22px; background: #111; border: 2px solid var(--white);
  }
  .order-button {
    position: absolute; left: 1010px; top: 109px; width: 69px; height: 38px;
    border-radius: 19px; background: var(--accent); border: 2px solid #e6e6e6;
    color: var(--white); text-align: center;
    font-family: "Lobster Two", cursive; font-style: italic; font-weight: 700;
    font-size: 13px; line-height: 1; padding-top: 9px;
  }
  .order-button small { display: block; font-size: 6px; margin-top: 1px; }
  .main-nav {
    position: absolute; top: 160px; left: 0; width: 1200px; height: 70px;
    background: var(--band);
  }
  .main-nav ul { list-style: none; position: relative; height: 100%; }
  .main-nav li {
    position: absolute; top: 23px;
    font-family: "Lobster Two", cursive; font-style: italic; font-weight: 700;
    font-size: 22px; color: var(--ink-soft);
  }
  .main-nav li.current { color: var(--accent); }
  .about-panel {
    position: absolute; left: 118px; top: 245px; width: 981px; height: 408px;
    background: var(--panel); border: 1px solid var(--panel-edge);
    padding: 36px 45px 0 46px;
  }
  .about-panel h1 {
    font-family: "Lobster Two", cursive; font-style: italic; font-weight: 700;
    font-size: 21px; color: var(--ink); margin-bottom: 14px;
  }
  .about-panel .lead { font-size: 19px; font-weight: 700; color: var(--ink); line-height: 30px; }
  .about-panel .body {
    font-size: 18px; line-height: 40px; text-align: justify; color: var(--ink);
  }
  .close-button {
    position: absolute; right: 0; top: 0; width: 35px; height: 34px;
    background: var(--close-grey); color: var(--white);
    font-size: 22px; font-weight: 700; text-align: center; line-height: 34px;
  }
  .photo-strip { position: absolute; top: 696px; left: 433px; display: flex; gap: 13px; }
  .photo-thumb {
    width: 61px; height: 61px; border-radius: 50%; border: 2px solid #e8e8e8;
  }
  .thumb-skyline { background: linear-gradient(#4f86c6, #9bb9d6 55%, #3d4f5e); }
  .thumb-food-a { background: radial-gradient(circle, #c7a27a, #6a4a33); }
  .thumb-food-b { background: radial-gradient(circle, #6f8a3a, #2a1a14); }
  .thumb-food-c { background: radial-gradient(circle, #c29a6e, #7a5a44); }
  .thumb-food-d { background: radial-gradient(circle, #e6d2bc, #9a6a4e); }
</style>
</head>
<body>
  <div class="backdrop" role="img" aria-label="Blurred photo of a plated dish on a dark wooden table with candlelight"></div>

  <header class="brand">
    <span class="brand-dot"></span>
    <span class="brand-name">Thimble Deli</span>
  </header>

  <div class="wifi-badge" role="img" aria-label="Free wi-fi badge"></div>
  <a class="order-button">Order Online<small>Now</small></a>

  <nav class="main-nav">
    <ul>
      <li style="left:117px">Home</li>
      <li style="left:210px">Menus</li>
      <li style="left:302px">Gallery</li>
      <li class="current" style="left:408px">About</li>
      <li style="left:503px">Media &amp; Events</li>
      <li style="left:675px">Hours &amp; Location</li>
      <li style="left:858px">Order Online</li>
      <li style="left:1003px">Contact Us</li>
    </ul>
  </nav>

  <section class="about-panel">
    <span class="close-button">X</span>
    <h1>About Us</h1>
    <p class="lead">Thimble Deli is a gourmet sandwich shop in Baltimore, MD USA.</p>
    <p class="body">We are due to open in about a month or so and we need a great web page that looks cool and is easy to use. Our Concept supports local farmers, ranchers, fishmongers &amp; purveyors. All of our menu items are made from scratch using fresh local ingredients.&nbsp; We are due to open in about a month or so and we need a great web page that looks cool and is easy to use. Our Concept supports local farmers, ranchers, fishmongers &amp; purveyors. All of our menu items are made from scratch using fresh local ingredients, scratch using fresh local ingredients.</p>
  </section>

  <div class="photo-strip">
    <span class="photo-thumb thumb-skyline" role="img" aria-label="City skyline over the harbor"></span>
    <span class="photo-thumb thumb-food-a" role="img" aria-label="Plated sandwich"></span>
    <span class="photo-thumb thumb-food-b" role="img" aria-label="Fresh salad"></span>
    <span class="photo-thumb thumb-food-c" role="img" aria-label="Plated sandwich"></span>
    <span class="photo-thumb thumb-food-d" role="img" aria-label="Sushi rolls"></span>
  </div>
</body>
</html>
```